Payment company requires web design

We need a web design for a new company based in Singapore.

The company focuses on providing 2 key products: 1) an alternative payment option (i.e. like plorix or quentabank options) on the traditional checkout process 2) a replacement/outsource of a merchants payment page. Key in the UX flow is a end customer dashboard that manages all payments.

We look to provide a simple, fluid and easy to use payment process. The dashboard is minimalistic that allows easy navigation, review of transactions and all available options through gamification.

The final design should communicate ease of use, flexibility and transparency.

Target Market(s)

The value is for the merchant - retail/travel/insurance companies. However its the merchant's end customers that are the target and who the UX is built for.

Industry/Entity Type

It Company

Logo Text

dravin

Number of Pages Required

5+ page

Colors
ec1f27

Requirements
Must have
• 7 pages mimicking UX flow
• payment page * 2 - 1) alternative payment type 2) outsource of merchants payment page to our business
• our landing page
• end customer verification page
• end customer registration
• customer dashboard
• UX flow in attached file
Nice to have
• open to ideas
• have asked for the logo to be added
• logo to have the colour red (chinese for prosperity)
• the company is all about flexibility, transparency in personal finance management with the option of instalment payments

```html
<!DOCTYPE html>
<html lang="en">
<head>
<meta charset="utf-8">
<title>dravin – The easy way to buy online</title>
<link rel="stylesheet" href="https://fonts.googleapis.com/css2?family=Open+Sans:ital,wght@0,400;0,600;0,700;1,400&family=Raleway:wght@400;600;700;800&family=Montserrat:wght@400;600;700&display=swap">
<style>
:root{
  --red:#ee2a2f;
  --red-bright:#ff3d3d;
  --navy:#2a3877;
  --ink:#4a4a4a;
  --muted:#6b6b6b;
  --rule:#e2e2e2;
  --footer:#0c0c1f;
  --white:#ffffff;
}
*{box-sizing:border-box;margin:0;padding:0}
html,body{width:1200px;height:2196px;overflow:hidden;background:var(--white)}
body{position:relative;font-family:"Open Sans",Arial,sans-serif;color:var(--ink)}
.abs{position:absolute}
.center-x{transform:translateX(-50%);text-align:center;white-space:nowrap}

/* hero */
.hero{position:absolute;left:0;top:0;width:1200px;height:474px;overflow:hidden;
  background:linear-gradient(100deg,#b8487e 0%,#c04d7c 25%,#8a4f8d 48%,#5f6fae 62%,#3a9ac8 80%,#2e86b5 100%)}
.hero-shade{position:absolute;inset:0;background:linear-gradient(180deg,rgba(60,20,60,.15),rgba(40,20,60,.35))}
.ad-slot{left:370px;top:22px;width:460px;height:57px;background:#ff1f1f;color:#fff;
  font-size:15px;display:flex;align-items:center;justify-content:center}
.brand{font-family:"Raleway",sans-serif;font-weight:800;font-size:38px;letter-spacing:-.5px;line-height:1}
.brand-hero{left:600px;top:104px;color:#fff}
.account{top:115px;height:20px;border:1px solid #fff;border-radius:10px;font-size:9px;
  color:#fff;display:flex;align-items:center;justify-content:center;letter-spacing:.3px;font-family:"Montserrat",sans-serif}
.account.my{left:810px;width:70px}
.account.reg{left:893px;width:54px;background:#fff;color:var(--navy)}
.hero-rule{left:330px;top:154px;width:540px;height:1px;background:rgba(255,255,255,.35)}
.nav a{position:absolute;top:172px;font-family:"Montserrat",sans-serif;font-weight:700;font-size:9px;color:#fff;text-decoration:none;letter-spacing:.3px}
.hero-title{left:600px;top:243px;color:#fff;font-weight:700;font-size:42px;line-height:45px;text-align:center;transform:translateX(-50%);white-space:nowrap}
.hero-sub{left:600px;top:344px;color:#fff;font-size:14.5px;line-height:21px}
.btn{background:var(--red-bright);color:#fff;border-radius:20px;display:flex;align-items:center;justify-content:center;
  font-family:"Montserrat",sans-serif;font-weight:600;font-size:9px;letter-spacing:.3px}
.hero-btn{left:555px;top:402px;width:92px;height:22px}
.dots{left:569px;top:453px;display:flex;gap:10px}
.dots span{width:8px;height:8px;border-radius:50%;background:rgba(255,255,255,.6)}
.dots span:first-child{background:#fff}

/* sections */
.rule{left:155px;width:888px;height:1px;background:var(--rule)}
.mark{width:20px;height:26px;background:var(--red)}
.section-title{font-family:"Raleway",sans-serif;font-weight:800;color:var(--navy);font-size:34px;line-height:1}
.about-text{left:254px;top:584px;width:694px;font-style:italic;font-size:12.3px;line-height:14px;text-align:center;color:var(--muted)}

.devices{left:176px;top:758px;width:388px;height:192px;border-radius:6px;
  background:linear-gradient(90deg,#2a2a2a 0%,#c04d7c 30%,#4f8ec0 60%,#e6e6e6 100%)}
.who-title{left:619px;top:733px;font-family:"Raleway",sans-serif;font-weight:800;font-size:22px;color:var(--navy);display:flex;align-items:baseline;gap:6px}
.who-title .name{color:var(--red);font-size:30px}
.who-text{left:619px;top:773px;width:352px;font-style:italic;font-size:12.3px;line-height:14px;color:var(--muted)}
.more-btn{left:619px;top:912px;width:92px;height:21px}

.feature{top:1022px;width:210px;transform:translateX(-50%);text-align:center}
.feature svg{display:block;margin:0 auto}
.feature h3{font-family:"Montserrat",sans-serif;font-weight:700;font-size:9.5px;color:var(--navy);margin-top:14px;letter-spacing:.2px}
.feature p{font-size:8.8px;line-height:13.5px;color:var(--muted);margin-top:7px}

.how-text{left:600px;top:1311px;font-size:16.5px;line-height:19px;color:#555}
.step{top:1391px;width:114px;height:114px;border:1.5px solid var(--red);border-radius:50%;display:flex;align-items:center;justify-content:center}
.step-arrow{top:1444px}
.step-caption{top:1519px;width:200px;transform:translateX(-50%);text-align:center;font-size:16.5px;line-height:19px;color:#555}

.ready{left:600px;top:1670px;font-family:"Raleway",sans-serif;font-size:24px;color:#333}
.ready-sub{left:600px;top:1703px;font-family:"Raleway",sans-serif;font-size:18px;color:#444}
.join-btn{left:513px;top:1751px;width:174px;height:31px;font-size:8.5px}

.partners{top:1921px}
.partner{position:absolute;top:1921px;transform:translateX(-50%);font-family:"Raleway",sans-serif;font-weight:700;font-size:24px;color:#8a8a8a;white-space:nowrap}

/* footer */
.footer{left:0;top:2018px;width:1200px;height:178px;background:var(--footer);color:#fff}
.footer h4{font-family:"Montserrat",sans-serif;font-weight:700;font-size:9px;letter-spacing:.3px}
.footer p{font-size:8.5px;line-height:15px;color:#d8d8d8}
.brand-footer{left:600px;top:2051px;color:#fff;font-size:36px}
.footer-rule{left:537px;top:2105px;width:126px;height:1px;background:rgba(255,255,255,.35)}
.socials{left:498px;top:2132px;display:flex;gap:13px}
.socials span{width:10px;height:10px;border-radius:50%;background:#fff}
.copyright{left:600px;top:2181px;font-size:7.5px;color:#cfcfcf}
</style>
</head>
<body>

<header class="hero" role="img" aria-label="Photo of a smiling couple with shopping bags and a laptop">
  <div class="hero-shade"></div>
</header>

<div class="abs ad-slot">Banner add 728x90</div>
<div class="abs brand brand-hero center-x">dravin</div>
<div class="abs account my">MY ACCOUNT</div>
<div class="abs account reg">REGISTER</div>
<div class="abs hero-rule"></div>
<nav class="nav">
  <a style="left:436px">HOME</a>
  <a style="left:501px">SERVICES</a>
  <a style="left:568px">INFORMATION</a>
  <a style="left:650px">CUSTOMERS</a>
  <a style="left:739px">FAQ&nbsp;<svg width="7" height="5" viewBox="0 0 7 5"><path d="M1 1l2.5 2.5L6 1" stroke="#fff" stroke-width="1.4" fill="none"/></svg></a>
</nav>
<h1 class="abs hero-title">DRAVIN, THE EASY WAY<br>TO BUY ONLINE</h1>
<p class="abs hero-sub center-x">Lorem ipsum dolor sit amet, consectetur adipiscing elit. Praesent commodo cursus magna<br>vel scelerisque nisi consectetur et.</p>
<div class="abs btn hero-btn">FIND OUT MORE</div>
<div class="abs dots"><span></span><span></span><span></span><span></span></div>

<!-- about -->
<div class="abs mark" style="left:590px;top:494px"></div>
<h2 class="abs section-title center-x" style="left:600px;top:535px">ABOUT US</h2>
<p class="abs about-text">Lorem ipsum dolor sit amet, consectetur adipisicing elit, sed do eiusmod tempor incididunt ut labore et dolore magna aliqua. Ut enim ad minim veniam, quis nostrud exercitation ullamco laboris nisi ut aliquip ex ea commodo consequat. Duis aute irure dolor in reprehenderit in voluptate velit esse cillum dolore eu fugiat nulla pariatur. Excepteur sint occaecat cupidatat non proident, sunt in culpa q, qui dolorem ipsum quia dolor sit amet, consectetur, adipisci velit, sed quia non numquam eius modi tempora incidunt ut labore et dolore magnam aliquam quaerat voluptatem.</p>
<div class="abs rule" style="top:694px"></div>

<!-- who is -->
<div class="abs devices" role="img" aria-label="Desktop, laptop, tablet and phone showing the website"></div>
<h2 class="abs who-title">WHO IS <span class="name">dravin</span> ?</h2>
<p class="abs who-text">Lorem ipsum dolor sit amet, consectetur adipisicing elit, sed do eiusmod tempor incididunt ut labore et dolore magna aliqua. Ut enim ad minim veniam, quis nostrud exercitation ullamco laboris nisi ut aliquip ex ea commodo consequat. Duis aute irure dolor in reprehenderit in voluptate velit esse cillum dolore eu fugiat nulla pariatur. Excepteur sint occaecat cupidatat non proident, sunt in culpa q, qui dolorem ipsum quia dolor sit amet, consectetur, adipisci velit, sed quia non numquam eius modi tempora incidunt ut labore et dolore magnam aliquam quaerat voluptatem.</p>
<div class="abs btn more-btn">MORE INFO</div>
<div class="abs rule" style="top:966px"></div>

<!-- features -->
<div class="abs feature" style="left:331px">
  <svg width="48" height="38" viewBox="0 0 48 38" fill="none" stroke="#ee2a2f" stroke-width="1.6"><rect x="2" y="2" width="44" height="28" rx="2"/><rect x="6" y="6" width="36" height="20"/><path d="M18 36h12M24 30v6"/></svg>
  <h3>EASY TO USE</h3>
  <p>Cras justo odio, dapibus ac facilisis in, egestas eget quam. Nullam quis risus eget urna mollis ornare vel eu leo. Donec ullamcorper nulla non metus auctor</p>
</div>
<div class="abs feature" style="left:600px">
  <svg width="30" height="38" viewBox="0 0 30 38" fill="none" stroke="#ee2a2f" stroke-width="1.6"><path d="M15 2a12 12 0 0 0-7 21.7V29h14v-5.3A12 12 0 0 0 15 2z"/><path d="M10 32h10M11 35h8M15 29v-9l-3-3M15 20l3-3"/></svg>
  <h3>MODERN PAYMENTS</h3>
  <p>Cras justo odio, dapibus ac facilisis in, egestas eget quam. Nullam quis risus eget urna mollis ornare vel eu leo. Donec ullamcorper nulla non metus auctor</p>
</div>
<div class="abs feature" style="left:870px">
  <svg width="48" height="38" viewBox="0 0 48 38" fill="none" stroke="#ee2a2f" stroke-width="1.6"><rect x="2" y="9" width="44" height="27" rx="2"/><path d="M17 9V3h14v6M2 20h44"/><rect x="21" y="17" width="6" height="6"/></svg>
  <h3>KEEP SAVED</h3>
  <p>Cras justo odio, dapibus ac facilisis in, egestas eget quam. Nullam quis risus eget urna mollis ornare vel eu leo. Donec ullamcorper nulla non metus auctor</p>
</div>
<div class="abs rule" style="top:1195px"></div>

<!-- how it works -->
<h2 class="abs section-title center-x" style="left:600px;top:1248px;font-weight:700">HOW IT WORKS?</h2>
<p class="abs how-text center-x">Lorem ipsum dolor sit amet, consectetur adipiscing elit. Vestibulum molestie augue dui, non tincidunt<br>neque fermentum in. Vivamus ultrices aliquam lacinia. Nullam et nunc in lacus consectetur posuere.</p>

<div class="abs step" style="left:334px">
  <svg width="36" height="40" viewBox="0 0 36 40" fill="#ee2a2f"><circle cx="18" cy="11" r="9"/><path d="M2 40v-8a10 10 0 0 1 10-10h12a10 10 0 0 1 10 10v8z"/></svg>
</div>
<svg class="abs step-arrow" style="left:482px" width="32" height="9" viewBox="0 0 32 9"><path d="M0 4.5h26" stroke="#ee2a2f" stroke-width="2.5"/><path d="M24 0l8 4.5-8 4.5z" fill="#ee2a2f"/></svg>
<div class="abs step" style="left:543px">
  <svg width="50" height="36" viewBox="0 0 50 36"><rect x="7" y="3" width="36" height="25" rx="2" fill="none" stroke="#ee2a2f" stroke-width="4"/><path d="M1 31h48v2a2 2 0 0 1-2 2H3a2 2 0 0 1-2-2z" fill="#ee2a2f"/></svg>
</div>
<svg class="abs step-arrow" style="left:692px" width="32" height="9" viewBox="0 0 32 9"><path d="M0 4.5h26" stroke="#ee2a2f" stroke-width="2.5"/><path d="M24 0l8 4.5-8 4.5z" fill="#ee2a2f"/></svg>
<div class="abs step" style="left:753px">
  <svg width="48" height="42" viewBox="0 0 48 42" fill="#ee2a2f"><path d="M0 2h9l2 6h36l-5 18H15L9 6H0z"/><path d="M14 29h29v4H12z"/><circle cx="18" cy="38" r="4"/><circle cx="38" cy="38" r="4"/></svg>
</div>
<p class="abs step-caption" style="left:391px">Lorem ipsum dolor sit amet, consectetur adipiscing elit. Vestibulum molestie .</p>
<p class="abs step-caption" style="left:600px">Lorem ipsum dolor sit amet, consectetur adipiscing elit. Vestibulum molestie .</p>
<p class="abs step-caption" style="left:810px">Lorem ipsum dolor sit amet, consectetur adipiscing elit. Vestibulum molestie .</p>
<div class="abs rule" style="top:1634px"></div>

<!-- call to action -->
<p class="abs ready center-x">Are You Ready to Start?</p>
<p class="abs ready-sub center-x">Click on the button below to become a member</p>
<div class="abs btn join-btn">JOIN TODAY!</div>
<div class="abs rule" style="top:1818px"></div>

<!-- partners -->
<h2 class="abs section-title center-x" style="left:600px;top:1861px">BUY ON</h2>
<span class="partner" style="left:209px">Norvale</span>
<span class="partner" style="left:366px">Callora</span>
<span class="partner" style="left:521px">Fabelry Store</span>
<span class="partner" style="left:679px">Wantly</span>
<span class="partner" style="left:836px">Roomhaven</span>
<span class="partner" style="left:993px">Bidmarket</span>

<!-- footer -->
<footer class="abs footer"></footer>
<h4 class="abs center-x" style="left:354px;top:2061px;color:#fff;font-family:'Montserrat',sans-serif;font-weight:700;font-size:9px">LOCATION</h4>
<p class="abs center-x" style="left:354px;top:2078px;font-size:8.5px;line-height:17px;color:#d8d8d8">88 Harbour Lane<br>Westvale, WV 55555</p>
<div class="abs brand brand-footer center-x">dravin</div>
<div class="abs footer-rule"></div>
<div class="abs socials"><span></span><span></span><span></span><span></span><span></span><span></span><span></span><span></span></div>
<h4 class="abs center-x" style="left:846px;top:2061px;color:#fff;font-family:'Montserrat',sans-serif;font-weight:700;font-size:9px">ABOUT DRAVIN</h4>
<p class="abs" style="left:756px;top:2078px;width:180px;text-align:center;font-size:8.5px;line-height:15px;color:#d8d8d8">Cras justo odio, dapibus ac facilisis in, egestas eget quam. Donec ullamcorper nulla non metus auctor fringilla.</p>
<p class="abs copyright center-x">Copyright © 2016. All Rights Reserved</p>

</body>
</html>
```